Swimming Pool Business Billboard

10' x 24' Billboard displaying company name, logo and phone number. Picture of swimming pool activity; kids playing , swimming, etc. Bullet points possibly shown: New Construction, Repairs, Weekly maintenance.

Industry/Entity Type

Swimming pool construction, repairs and maintenance.

Font styles to use
Sans Serif

Colors
0054AA
0677BA
7BADD7
CADEEF
E8F1F8

Requirements
Must have
• Rusty & Calder Pembrook, RUSTY'S POOLS & Service,
Nice to have
• Prefer to have my last name "Pembrook" above the word "POOLS" only in smaller print so that "RUSTYS POOLS" is distinguished.

```html
<!DOCTYPE html>
<html lang="en">
<head>
<meta charset="UTF-8">
<title>Rusty's Pools &amp; Services Billboard</title>
<link rel="stylesheet" href="https://fonts.googleapis.com/css2?family=Crimson+Text:ital@1&family=Roboto+Slab:wght@800&family=Montserrat:wght@500;700;800&display=swap">
<style>
  :root {
    --page-bg: #b3b3b3;
    --board-white: #ffffff;
    --navy: #173f73;
    --brand-blue: #0054AA;
    --mid-blue: #0677BA;
    --sky-blue: #7BADD7;
    --pale-blue: #CADEEF;
    --mist-blue: #E8F1F8;
    --photo-green: #7f9a5c;
    --photo-light: #c9d8b4;
  }
  html, body {
    margin: 0;
    padding: 0;
    width: 1034px;
    height: 1200px;
    overflow: hidden;
    background: var(--page-bg);
  }
  .billboard {
    position: absolute;
    left: 17px;
    top: 391px;
    width: 1000px;
    height: 417px;
    display: block;
  }
  .owner-name {
    font-family: "Crimson Text", Georgia, serif;
    font-style: italic;
    font-size: 38px;
    fill: var(--navy);
  }
  .company-name {
    font-family: "Roboto Slab", Georgia, serif;
    font-weight: 800;
    font-size: 30px;
    fill: var(--navy);
  }
  .phone-number {
    font-family: "Montserrat", Arial, sans-serif;
    font-weight: 800;
    font-size: 58px;
    letter-spacing: -2px;
    fill: var(--navy);
    stroke: var(--board-white);
    stroke-width: 2px;
    paint-order: stroke;
  }
  .service-item {
    font-family: "Montserrat", Arial, sans-serif;
    font-weight: 500;
    font-size: 30px;
    letter-spacing: 1px;
    fill: var(--navy);
  }
  .service-star {
    font-family: "Montserrat", Arial, sans-serif;
    font-size: 18px;
    fill: var(--navy);
  }
  .brand-mark-text {
    font-family: "Montserrat", Arial, sans-serif;
    font-weight: 700;
    font-size: 10px;
    fill: var(--navy);
  }
</style>
</head>
<body>
<svg class="billboard" viewBox="0 0 1000 417" xmlns="http://www.w3.org/2000/svg">
  <defs>
    <linearGradient id="photoTones" x1="0" y1="0" x2="0" y2="1">
      <stop offset="0" stop-color="var(--photo-light)"/>
      <stop offset="0.55" stop-color="var(--photo-green)"/>
      <stop offset="1" stop-color="#5f7a3e"/>
    </linearGradient>
  </defs>

  <rect class="board-surface" x="0" y="0" width="1000" height="417" fill="var(--board-white)"/>

  <rect class="phone-band" x="0" y="153" width="740" height="70" fill="var(--mist-blue)"/>
  <rect class="bottom-band" x="0" y="392" width="500" height="25" fill="var(--pale-blue)"/>

  <polygon class="photo-area" role="img" aria-label="Photo of children holding hands and playing in a circle on a sunny lawn"
           points="727,0 1000,0 1000,417 448,417" fill="url(#photoTones)"/>

  <g class="photo-slashes" stroke="var(--board-white)" stroke-width="3">
    <line x1="862" y1="0" x2="583" y2="417"/>
    <line x1="962" y1="0" x2="683" y2="417"/>
    <line x1="1000" y1="50" x2="755" y2="417"/>
    <line x1="1000" y1="290" x2="915" y2="417"/>
  </g>

  <text class="owner-name" x="30" y="68">Rusty Pembrook</text>
  <text class="company-name" x="30" y="118">RUSTY'S POOLS &amp; Services</text>

  <g class="brand-mark">
    <circle cx="602" cy="40" r="22" fill="var(--navy)"/>
    <text class="brand-mark-text" x="602" y="78" text-anchor="middle">RUSTY'S</text>
    <text class="brand-mark-text" x="602" y="90" text-anchor="middle">POOLS</text>
  </g>

  <text class="phone-number" x="33" y="212">912-555-0147</text>

  <g class="service-list">
    <text class="service-star" x="32" y="272">★</text>
    <text class="service-item" x="54" y="276">Repairs</text>
    <text class="service-star" x="32" y="315">★</text>
    <text class="service-item" x="54" y="319">New Construction</text>
    <text class="service-star" x="32" y="361">★</text>
    <text class="service-item" x="54" y="365">Weekly maintenance</text>
  </g>
</svg>
</body>
</html>
```